New website design

Hello again, we need you to create a basic, standard website with a homepage, 'contact us' page with reply form, 'pricing page' and 'about us' page. We would like to see most design elements carried over from www.tallowpine.com, our primary website. You can also use the front page of the attached brochure as inspiration for the homepage. The second attachment shows the pricing page (image on the right) with vertical columns - that's a good template for you to use on the pricing page for the website. The third attachment contains the text for the pricing page...just don't use that layout, try and duplicate the vertical layout example.
Target Market(s)
hospitals/medical care facilities
Coding
Coded - Design and coding required
Number of Pages Required
4 page
Look and feel

```html
<!DOCTYPE html>
<html lang="en">
<head>
<meta charset="utf-8">
<title>Tallowpine Medical Inc.</title>
<link href="https://fonts.googleapis.com/css2?family=Montserrat:wght@400;500;600;700&display=swap" rel="stylesheet">
<style>
:root{
  --frame:#1c7bb0;
  --navy:#0f3f66;
  --deep:#0b2f4f;
  --brand:#1b79b4;
  --brand-light:#3a9bd3;
  --ink:#1a1a1a;
  --muted:#555;
  --mist:#e7ecf0;
  --field:#eef1f4;
  --white:#fff;
}
*{margin:0;padding:0;box-sizing:border-box}
html,body{width:1200px;height:4517px;overflow:hidden}
body{background:var(--frame);font-family:'Montserrat',sans-serif;color:var(--ink);position:relative}
.page{position:absolute;left:53px;top:61px;width:1095px;height:4412px;background:var(--white);overflow:hidden}
.abs{position:absolute}
.accent{color:var(--brand)}
.photo{position:absolute}
.btn{position:absolute;background:var(--brand);color:var(--white);font-size:12px;font-weight:500;display:flex;align-items:center;justify-content:center}

/* hero */
.hero{position:absolute;left:0;top:0;width:1095px;height:600px;background:linear-gradient(100deg,#0e3f6a 0%,#1c5f93 45%,#5e9ccc 75%,#a9cbe6 100%)}
.brand{position:absolute;display:flex;align-items:center;gap:8px;font-weight:500;color:var(--white)}
.brand .dot{width:22px;height:22px;border-radius:50%;background:var(--brand-light)}
.nav{position:absolute;top:22px;left:507px;display:flex;gap:27px;font-size:11px;color:var(--white);align-items:center}
.hero h1{position:absolute;left:184px;top:180px;font-size:38px;font-weight:700;color:var(--white)}
.hero p{position:absolute;left:184px;top:250px;width:370px;font-size:15px;line-height:1.25;color:var(--white)}

/* about */
.section-title{font-size:21px;font-weight:700}
.about-text{position:absolute;left:643px;top:719px;width:268px;font-size:10px;line-height:1.6;color:var(--muted)}

/* mist band */
.intro{position:absolute;left:0;top:1172px;width:1095px;text-align:center}
.intro h2{font-size:20px;font-weight:700;line-height:1.25}
.intro p{margin:42px auto 0;width:480px;font-size:11px;line-height:1.3}
.q-card{position:absolute;top:1363px;height:204px;background:var(--white);text-align:center;font-size:12px;font-weight:500;line-height:1.25;padding:0 26px}
.q-card .ico{width:52px;height:52px;border-radius:50%;background:var(--brand);margin:40px auto 34px;display:flex;align-items:center;justify-content:center}

/* tiles */
.tile{position:absolute;color:var(--white)}
.tile h3{font-size:20px;font-weight:700;margin-bottom:14px}
.tile p{font-size:10.5px;line-height:1.55}

/* pricing */
.price-card{position:absolute;top:2477px;width:200px;height:324px;background:var(--white);border-radius:6px;text-align:center;padding-top:15px}
.price-card h4{font-size:13px;font-weight:700;line-height:1.1}
.price-card h4 span{color:var(--brand)}
.pill{width:106px;height:44px;margin:16px auto 14px;border-radius:22px;background:var(--deep);color:var(--white);font-weight:700;font-size:15px;display:flex;align-items:center;justify-content:center;box-shadow:0 0 0 3px #9cc4de}
.price-card h5{font-size:9.5px;font-weight:700;line-height:1.2;padding:0 22px}
.price-card p{font-size:8px;line-height:1.3;color:#777;padding:0 22px;margin-top:14px}
.details{position:absolute;left:50px;bottom:-16px;width:100px;height:32px;border-radius:16px;background:var(--brand);color:var(--white);font-size:11px;font-weight:600;display:flex;align-items:center;justify-content:center;box-shadow:0 0 0 3px #9cc4de}

/* faq */
.faq{position:absolute;left:184px;width:726px;border:1px solid #eef0f2;padding:0 28px 0 62px;font-size:13.5px;font-weight:500}
.faq .q{position:absolute;left:24px;width:22px;height:22px;border-radius:50%;background:var(--brand);color:var(--white);font-size:12px;font-weight:700;display:flex;align-items:center;justify-content:center}
.faq .tog{position:absolute;right:22px;font-size:22px;font-weight:600}
.faq p{font-size:12.5px;font-weight:400;line-height:1.3;margin-top:10px}

/* contact */
.field{position:absolute;left:631px;width:279px;height:28px;background:var(--field);border-radius:3px;font-size:9px;color:#999;padding:10px 0 0 20px}

/* footer */
.footer-nav{position:absolute;left:0;top:4050px;width:1095px;display:flex;justify-content:center;gap:30px;font-size:15px;color:var(--white)}
.fcol{position:absolute;top:4132px;color:var(--white)}
.fcol h6{font-size:13px;font-weight:500;margin-bottom:18px}
.fcol li{list-style:none;font-size:9px;line-height:1.3;margin-bottom:20px}
.contact-row{display:flex;gap:16px;margin-bottom:18px;font-size:9px;line-height:1.35}
.contact-row i{width:16px;height:16px;flex:none;display:flex;align-items:center;justify-content:center}
.social{display:flex;gap:11px;margin-top:14px}
.social span{width:26px;height:26px;border-radius:50%;background:var(--white)}
</style>
</head>
<body>
<div class="page">

  <!-- HERO -->
  <div class="hero">
    <div class="photo" role="img" aria-label="Lab technician in protective cap and mask looking into a microscope" style="left:560px;top:0;width:535px;height:600px;background:radial-gradient(ellipse at 60% 40%,rgba(200,225,245,.55),rgba(30,90,140,0) 70%)"></div>
    <div class="brand" style="left:184px;top:13px;font-size:20px"><span class="dot"></span>Tallowpine Medical</div>
    <div class="nav"><span>Home</span><span>Services</span><span>About Us</span><span>Support</span><span class="btn" style="position:static;width:105px;height:28px;font-size:11px">Contact Us</span></div>
    <h1>Tallowpine Medical Inc.</h1>
    <p>Offers efficient and FDA compliant assembly, packaging and in-house Hydrogen Peroxide Gas Plasma (HPGP) specific,</p>
    <div class="btn" style="left:184px;top:341px;width:124px;height:36px;font-size:13px">Read More</div>
  </div>
  <svg class="abs" style="left:0;top:480px" width="1095" height="160" viewBox="0 0 1095 160">
    <path d="M0 60 Q520 110 1095 45 L1095 160 L0 160Z" fill="var(--brand)"/>
    <path d="M0 80 Q520 150 1095 75 L1095 160 L0 160Z" fill="#fff"/>
  </svg>

  <!-- ABOUT -->
  <div class="photo" role="img" aria-label="Laboratory staff at work, framed in a round crop" style="left:201px;top:658px;width:334px;height:334px;border-radius:50%;background:radial-gradient(circle at 40% 45%,#c9d8e4,#6f8ea8 60%,#2c4c6a)"></div>
  <div class="abs section-title" style="left:643px;top:676px">About <span class="accent">US</span></div>
  <p class="about-text">Tallowpine Medical Inc. offers efficient and FDA compliant assembly, packaging and in-house Hydrogen Peroxide Gas Plasma (HPGP) specific, as well as contract irradiation (gamma and e-beam) sterilization services for the medical device industry. Validation services for manufacturing processes, packaging, and sterilization are customized to product specific requirements. The company is dedicated to industrial sterilization requirements and meeting the highest of industry standards; FDA registered; ISO 13485:2016 Certified; Audited in accordance with ISO 14937:2009 and compliant with ISO 14644-1 CLASS 7 (Class 10,000) Cleanrooms.</p>
  <div class="btn" style="left:643px;top:949px;width:106px;height:30px;font-size:11px">Contact Us</div>

  <!-- MIST BAND -->
  <svg class="abs" style="left:0;top:1040px" width="1095" height="680" viewBox="0 0 1095 680">
    <path d="M0 80 Q550 -10 1095 85 L1095 600 Q550 690 0 595Z" fill="#dde9f2"/>
    <path d="M0 95 Q550 20 1095 100 L1095 585 Q550 665 0 580Z" fill="var(--mist)"/>
  </svg>
  <div class="intro">
    <h2>Certified diagnostic and <span class="accent">repair services</span><br><span class="accent">for your</span> biomedical equipment</h2>
    <p>Today's medical technicians are constantly pressured productivity and minimize unexpected downtimes . this reqires easy access to technical product knowledge and fastexpert support , however</p>
  </div>
  <div class="q-card" style="left:184px;width:233px"><div class="ico"><svg width="24" height="22" viewBox="0 0 24 22"><rect x="2" y="5" width="20" height="15" rx="2" fill="none" stroke="#fff" stroke-width="2"/><path d="M8 5V2h8v3M12 9v7M8.5 12.5h7" stroke="#fff" stroke-width="2" fill="none"/></svg></div>Who do you contact in case of unexpected device malfunction</div>
  <div class="q-card" style="left:429px;width:235px;box-shadow:0 6px 16px rgba(0,0,0,.12)"><div class="ico"><svg width="24" height="24" viewBox="0 0 24 24"><circle cx="10" cy="8" r="4" fill="none" stroke="#fff" stroke-width="2"/><path d="M3 21c0-4 3-7 7-7s7 3 7 7" stroke="#fff" stroke-width="2" fill="none"/><circle cx="19" cy="6" r="3" fill="none" stroke="#fff" stroke-width="1.6"/></svg></div>What are the capabilities of the technician you call?</div>
  <div class="q-card" style="left:677px;width:233px"><div class="ico"><svg width="18" height="24" viewBox="0 0 18 24"><path d="M2 2h14M2 22h14M4 2c0 6 10 8 10 10S4 16 4 22M14 2c0 6-10 8-10 10s10 4 10 10" stroke="#fff" stroke-width="2" fill="none"/></svg></div>Is there a lengthy lead-time before service is performed</div>

  <!-- TILES -->
  <div class="photo" role="img" aria-label="Gloved hands handling a medical instrument" style="left:184px;top:1788px;width:347px;height:437px;background:linear-gradient(180deg,#cfd6dc 0%,#8e9aa5 45%,#1d2328 100%)"></div>
  <div class="tile" style="left:228px;top:2043px;width:260px"><h3>Our <span class="accent">Facility</span></h3><p>Our modern 20,000 square foot facility was designed to exceed today's regulatory requirements and has over 2500 square feet of cleanroom and support area designed to provide a high quality environment for assembly and packaging of Medical Devices.</p></div>
  <div class="photo" role="img" aria-label="Aerial view of an industrial facility with solar roofs" style="left:542px;top:1788px;width:368px;height:214px;background:linear-gradient(180deg,#7b8d9b 0%,#475866 50%,#111a22 100%)"></div>
  <div class="tile" style="left:570px;top:1893px;width:290px"><h3 style="margin-bottom:10px">Our <span class="accent">Location</span></h3><p>Tallowpine Medical is located on the beautiful Central Coast of California mid-way between San Francisco and Los Angeles.</p></div>
  <div class="photo" role="img" aria-label="Technician working with lab samples" style="left:542px;top:2012px;width:368px;height:213px;background:linear-gradient(180deg,#a5b3bf 0%,#5b6b78 50%,#141c24 100%)"></div>
  <div class="tile" style="left:570px;top:2093px;width:290px"><h3 style="margin-bottom:10px">Our <span class="accent">Expertise</span></h3><p>Tallowpine Medical's areas of expertise include manufacturing and packaging specialties, process and sterility validation studies, environmental controls, and bringing new products to market.</p></div>

  <!-- PRICING -->
  <svg class="abs" style="left:0;top:2270px" width="1095" height="680" viewBox="0 0 1095 680">
    <defs><linearGradient id="pricingFill" x1="0" y1="0" x2="0" y2="1"><stop offset="0" stop-color="#134a78"/><stop offset="1" stop-color="#0d3558"/></linearGradient></defs>
    <path d="M0 50 Q550 -20 1095 40 L1095 615 Q550 700 0 620Z" fill="var(--brand)"/>
    <path d="M0 70 Q550 5 1095 60 L1095 595 Q550 675 0 600Z" fill="url(#pricingFill)"/>
  </svg>
  <div class="abs" style="left:0;top:2392px;width:1095px;text-align:center;font-size:19px;font-weight:700;color:#fff">Our <span style="color:var(--brand-light)">Pricing</span></div>
  <div class="price-card" style="left:184px"><h4>On site<br><span>Unschedules</span></h4><div class="pill">$225/hour</div><h5>Emergency priority service-technician typically on-premises</h5><p>Electronic device failure is one of the few certainties in life. We can't know when mission critical devices will malfunction, but preparation and planning lead to positive outcomes. Call us now for your free pre-service inspection so we are both prepared for your next emergency service.</p><div class="details">Details</div></div>
  <div class="price-card" style="left:445px"><h4>On site<br><span>Unschedules</span></h4><div class="pill">$195/hour</div><h5>Planned service and/or recurring maintenance - technicians required on premises</h5><p>Following the proper maintenance schedule can help reduce catastrophic failures, increase the lifespan of your biomedical devices, and typically results in significant cost savings.</p><div class="details">Details</div></div>
  <div class="price-card" style="left:706px"><h4>Off site<br><span>Unschedules</span></h4><div class="pill">$175/hour</div><h5>Emergency priority service of equipment that can be shipped to our repair center</h5><p>Anticipate the unexpected - put your plan in place now to address medical device failures. Whether you're facing a shortage of hospital resources or a complicated repair that can't be completed in-house, we'll prioritize your equipment for the shortest lead-time.</p><div class="details">Details</div></div>
  <div class="abs" style="left:516px;top:2858px;display:flex;gap:12px">
    <span style="width:11px;height:11px;border-radius:50%;background:#2a6c9c"></span>
    <span style="width:11px;height:11px;border-radius:50%;background:#fff"></span>
    <span style="width:11px;height:11px;border-radius:50%;background:#2a6c9c"></span>
  </div>

  <!-- FAQ -->
  <div class="abs" style="left:0;top:3028px;width:1095px;text-align:center;font-size:20px;font-weight:700">frequently <span class="accent">asked questions</span></div>
  <div class="faq" style="top:3114px;height:102px;padding-top:16px"><span class="q" style="top:16px">?</span><span class="tog" style="top:10px">-</span>What does LOREM mean?<p>'Lorem ipsum dolor sit amet, consectetur adipisici elit...' (complete text) is dummy text that is not meant to mean anything. It is used as a placeholder in magazine layouts, for example, in order to give an impression of the finished document.</p></div>
  <div class="faq" style="top:3233px;height:44px;padding-top:13px"><span class="q" style="top:11px">?</span><span class="tog" style="top:7px">+</span>Where can I subscribe to your newsletter?</div>
  <div class="faq" style="top:3298px;height:44px;padding-top:13px"><span class="q" style="top:11px">?</span><span class="tog" style="top:14px">+</span>Where can in edit my address?</div>
  <div class="faq" style="top:3363px;height:46px;padding-top:13px"><span class="q" style="top:11px">?</span><span class="tog" style="top:16px">+</span>Can I order a free copy of a magazine to sample?</div>

  <!-- CONTACT -->
  <div class="abs" style="left:195px;top:3472px;width:346px;height:346px;border-radius:50%;background:var(--brand)"></div>
  <div class="photo" role="img" aria-label="Smiling lab scientist in a white coat at a workbench" style="left:207px;top:3484px;width:322px;height:322px;border-radius:50%;background:radial-gradient(circle at 45% 40%,#e9eef2,#b7c6d2 55%,#7d93a6)"></div>
  <div class="abs section-title" style="left:631px;top:3475px">Contact <span class="accent">Us</span></div>
  <div class="abs" style="left:631px;top:3520px;font-size:11px;font-weight:500">Get a Free Consultation</div>
  <div class="field" style="top:3558px">Full name</div>
  <div class="field" style="top:3597px">Email Id</div>
  <div class="field" style="top:3635px">Company Name</div>
  <div class="field" style="top:3675px;height:86px">Message.....</div>
  <div class="btn" style="left:631px;top:3773px;width:279px;height:32px;font-size:13px;border-radius:3px">Send Messages</div>

  <!-- FOOTER -->
  <svg class="abs" style="left:0;top:3860px" width="1095" height="552" viewBox="0 0 1095 552" preserveAspectRatio="none">
    <defs><linearGradient id="footFill" x1="0" y1="0" x2="0" y2="1"><stop offset="0" stop-color="#134a78"/><stop offset="1" stop-color="#0b2f4f"/></linearGradient></defs>
    <path d="M0 45 Q550 -15 1095 30 L1095 552 L0 552Z" fill="var(--brand)"/>
    <path d="M0 70 Q550 15 1095 55 L1095 552 L0 552Z" fill="url(#footFill)"/>
  </svg>
  <div class="brand" style="left:430px;top:3982px;font-size:26px"><span class="dot" style="width:28px;height:28px"></span>Tallowpine Medical</div>
  <div class="footer-nav"><span>Home</span><span>Services</span><span>About Us</span><span>Support</span><span>Contact Us</span></div>

  <div class="fcol" style="left:184px;width:200px">
    <h6 style="margin-bottom:24px">Tallowpine Medical Inc.</h6>
    <div class="contact-row"><i><svg width="12" height="16" viewBox="0 0 12 16"><path d="M6 15S1 9 1 6a5 5 0 0110 0c0 3-5 9-5 9z" fill="#fff"/><circle cx="6" cy="6" r="2" fill="#134a78"/></svg></i><span>418 Cedar Loop,<br>Marrow Bay, CA 90210</span></div>
    <div class="contact-row"><i><svg width="14" height="14" viewBox="0 0 14 14"><path d="M3 1l3 3-2 2c1 2 2 3 4 4l2-2 3 3-2 2C6 13 1 8 1 3z" fill="#fff"/></svg></i><span>Phone:<br>(555) 201-4410</span></div>
    <div class="contact-row"><i><svg width="14" height="14" viewBox="0 0 14 14"><rect x="1" y="5" width="12" height="7" rx="1" fill="#fff"/><rect x="4" y="1" width="6" height="5" fill="#fff"/></svg></i><span>Fax:<br>(555) 201-4422</span></div>
    <div class="contact-row"><i><svg width="14" height="12" viewBox="0 0 14 12"><rect x="1" y="1" width="12" height="10" rx="1" fill="#fff"/><path d="M1 2l6 5 6-5" stroke="#134a78" fill="none"/></svg></i><span>E-mail:<br>info@tallowpine.com</span></div>
  </div>
  <div class="fcol" style="left:410px"><h6>Services</h6><ul><li>Sterilization</li><li>Packaging</li><li>Contract Manufacturing</li><li>New Product Introduction</li><li>Validations</li></ul></div>
  <div class="fcol" style="left:598px"><h6>Services</h6><ul><li>Shipping Option</li><li>My Wishlist</li><li>My Account</li><li>Return Policy</li><li>Product Categories</li></ul></div>
  <div class="fcol" style="left:771px;width:140px">
    <h6 style="font-weight:600;margin-bottom:36px">Subscribe Now</h6>
    <div style="height:28px;background:#fff;border-radius:3px;color:#333;font-size:8px;padding:10px 0 0 14px">Enter Email Id</div>
    <div style="height:28px;margin-top:16px;background:var(--brand);border-radius:3px;font-size:9.5px;font-weight:600;display:flex;align-items:center;justify-content:center">Get Started</div>
    <div class="social"><span></span><span></span><span></span><span></span></div>
  </div>
  <div class="abs" style="left:0;top:4376px;width:1095px;text-align:center;font-size:8px;color:#fff">© 2021 Tallowpine Medical, Inc. - 07-076-0075 rev. 03</div>
</div>
</body>
</html>
```